Modernize Cleaning Chemical Product Labels

I am looking to modernise our product labels.
We are a cleaning chemical manufacture predominately in the commercial cleaning industry.
I would like for the labels to be available in at least 6 colours, red, green, blue, yellow, purple and orange.
Design can be as small as 270mm x 140mm up to 340mm x 165mm. Current label dimensions 275mm x 165mm
I have attached some of our current labels and our logo and also some competitors labels

Colors
0054AA
0677BA
7BADD7
CADEEF
E8F1F8
00AB8E
00BBA5
67D7C9
C6EFE9
E9F9F6
FFF300
FFF600
FEFA6F
FFFEC7
FFFEE8
F0912C
F2A743
F7CA91
FBE8D2
FDF5EE
EB3D1F
EC4F4E
F09395
F8D3D4
FCEDEE
A7469A
B969AE
D3A5CF
EDDBEB
F8F0F9

```html
<!DOCTYPE html>
<html lang="en">
<head>
<meta charset="utf-8">
<title>Hartwell Brilliant – Premium Dishwashing Detergent Label</title>
<link href="https://fonts.googleapis.com/css2?family=Arimo:wght@400;700&family=Archivo:wght@800;900&family=Oswald:wght@600;700&display=swap" rel="stylesheet">
<style>
  :root {
    --navy: #124683;
    --teal: #3bc4cc;
    --teal-light: #7fdde2;
    --ink: #111111;
    --paper: #ffffff;
  }
  * { margin: 0; padding: 0; box-sizing: border-box; }
  html, body { width: 1200px; height: 720px; overflow: hidden; background: var(--paper); }
  body { font-family: "Arimo", Arial, sans-serif; color: var(--ink); }
  .label { position: relative; width: 1200px; height: 720px; overflow: hidden; }

  /* hazard block */
  .hazard-icon { position: absolute; left: 86px; top: 46px; width: 108px; height: 108px; }
  .hazard-statements, .warning-notes {
    position: absolute; left: 10px; width: 260px; text-align: center;
    font-size: 9.4px; line-height: 12.2px; text-transform: uppercase;
  }
  .hazard-statements { top: 158px; }
  .warning-title {
    position: absolute; left: 10px; width: 260px; top: 216px; text-align: center;
    font-family: "Oswald", sans-serif; font-weight: 700; font-size: 27px; line-height: 34px; letter-spacing: 0.5px;
  }
  .warning-notes { top: 248px; }

  /* brand */
  .brand-name {
    position: absolute; left: 330px; top: 66px; width: 540px; text-align: center;
    font-family: "Archivo", sans-serif; font-weight: 900; font-size: 72px; line-height: 80px; letter-spacing: 7px; color: var(--navy);
  }
  .product-name { position: absolute; left: 296px; top: 178px; width: 615px; height: 106px; }
  .product-name text { font-family: "Archivo", sans-serif; font-weight: 900; fill: var(--teal); }
  .volume {
    position: absolute; left: 1010px; top: 200px; width: 100px; text-align: center;
    font-family: "Oswald", sans-serif; font-weight: 700; font-size: 56px; line-height: 64px;
  }

  /* pattern areas */
  .pattern { position: absolute; background: linear-gradient(135deg, var(--teal) 0%, var(--teal-light) 45%, var(--navy) 100%); }
  .pattern-left-edge   { left: 0; top: 331px; width: 34px; height: 389px; }
  .pattern-left-top    { left: 70px; top: 331px; width: 280px; height: 30px; opacity: .55; }
  .pattern-left-bottom { left: 0; top: 694px; width: 315px; height: 26px; }
  .pattern-centre-left { left: 262px; top: 331px; width: 198px; height: 363px; }
  .pattern-centre-right{ left: 747px; top: 331px; width: 196px; height: 389px; }
  .pattern-right-top   { left: 943px; top: 331px; width: 257px; height: 30px; }
  .pattern-right-edge  { left: 1170px; top: 361px; width: 30px; height: 359px; }
  .pattern-right-bottom{ left: 980px; top: 694px; width: 190px; height: 26px; }

  /* info columns */
  .info-column { position: absolute; font-size: 10.2px; line-height: 12.3px; }
  .info-column p { margin-bottom: 12px; }
  .info-column b { font-weight: 700; }
  .uses-column { left: 44px; top: 391px; width: 214px; }
  .dilutions-title { text-align: center; font-weight: 700; font-size: 13px; line-height: 16px; margin: 6px 0 14px; }
  .safety-column { left: 954px; top: 391px; width: 214px; }
  .poison-line { font-weight: 700; }
  .rash-title { font-weight: 700; font-size: 13px; line-height: 15px; }
  .composition {
    position: absolute; left: 954px; top: 620px; width: 206px; text-align: center;
    font-family: "Oswald", sans-serif; font-weight: 600; font-size: 15px; line-height: 18.5px;
  }

  /* centre panel */
  .product-type {
    position: absolute; left: 470px; top: 346px; width: 302px; text-align: center;
    font-family: "Oswald", sans-serif; font-weight: 700; font-size: 38px; line-height: 37px;
  }
  .product-sub { position: absolute; left: 470px; top: 466px; width: 302px; text-align: center; font-size: 22px; line-height: 26px; letter-spacing: 0.5px; }
  .feature-list { position: absolute; left: 412px; top: 512px; width: 320px; list-style: none; text-align: center; }
  .feature-list li { font-size: 18.5px; line-height: 27.8px; white-space: nowrap; }
  .feature-list svg { width: 13px; height: 12px; margin-right: 4px; vertical-align: 0; }
  .company-address { position: absolute; left: 420px; top: 668px; width: 360px; text-align: center; font-size: 12px; line-height: 14.6px; }
</style>
</head>
<body>
<main class="label">

  <svg class="hazard-icon" viewBox="0 0 108 108" role="img" aria-label="Hazard exclamation pictogram">
    <polygon points="54,4 104,54 54,104 4,54" fill="none" stroke="#111" stroke-width="6"/>
    <path d="M47 28 Q54 22 61 28 L57 66 H51 Z" fill="#111"/>
    <circle cx="54" cy="76" r="6.5" fill="#111"/>
  </svg>
  <p class="hazard-statements">Causes skin irritation.<br>May cause<br>an allergic skin reaction.</p>
  <h2 class="warning-title">WARNING</h2>
  <p class="warning-notes">Not to be taken<br>Keep out of reach of children<br>Read safety directions before opening</p>

  <div class="brand-name">HARTWELL</div>
  <svg class="product-name" viewBox="0 0 615 106">
    <text x="0" y="102" font-size="138" textLength="615" lengthAdjust="spacingAndGlyphs">BRILLIANT</text>
  </svg>
  <div class="volume">5 L</div>

  <div class="pattern pattern-left-edge" role="img" aria-label="Teal and navy hexagon pattern"></div>
  <div class="pattern pattern-left-top" role="img" aria-label="Teal and navy hexagon pattern"></div>
  <div class="pattern pattern-left-bottom" role="img" aria-label="Teal and navy hexagon pattern"></div>
  <div class="pattern pattern-centre-left" role="img" aria-label="Cluster of teal and navy hexagons"></div>
  <div class="pattern pattern-centre-right" role="img" aria-label="Cluster of teal and navy hexagons"></div>
  <div class="pattern pattern-right-top" role="img" aria-label="Teal and navy hexagon pattern"></div>
  <div class="pattern pattern-right-edge" role="img" aria-label="Teal and navy hexagon pattern"></div>
  <div class="pattern pattern-right-bottom" role="img" aria-label="Teal and navy hexagon pattern"></div>

  <section class="info-column uses-column">
    <p><b>USES:</b> Hand dishwashing, floors, kitchens, walls, tiles, bathroom and all painted surfaces.</p>
    <p>This product is a highly efficient, bio-degradable liquid detergent with a neutral pH, designed to achieve optimum results on a cost performance basis. It is a unique blend of ionic and non-ionic surfactants coupled with coconut oil derivatives to produce a high solids detergent with excellent streak-free rinsing properties.</p>
    <p><b>APPLICATIONS:</b> Hand dishwashing, floors, walls, benches, cars, house- washing (interior and exterior) and hand washing of fine fabrics.</p>
    <h3 class="dilutions-title">DILUTIONS</h3>
    <p><b>5 - 10ml</b> per <b>10 Litres</b> for dishwashing <b>(1:1000)</b><br><b>50 -150ml</b> per <b>10 litres</b> for floors, walls, cars, caravans, houses etc. <b>(5-15:1000)</b></p>
  </section>

  <h1 class="product-type">PREMIUM<br>DISHWASHING<br>DETERGENT</h1>
  <div class="product-sub">BIODEGRADABLE</div>
  <ul class="feature-list">
    <li><svg viewBox="0 0 13 12"><polygon points="3,0 10,0 13,6 10,12 3,12 0,6" fill="#3bc4cc"/></svg>High Solids Content</li>
    <li><svg viewBox="0 0 13 12"><polygon points="3,0 10,0 13,6 10,12 3,12 0,6" fill="#3bc4cc"/></svg>Only 5 to 10mLs per 10L Wash</li>
    <li><svg viewBox="0 0 13 12"><polygon points="3,0 10,0 13,6 10,12 3,12 0,6" fill="#3bc4cc"/></svg>Grease and Oil Cutters</li>
    <li><svg viewBox="0 0 13 12"><polygon points="3,0 10,0 13,6 10,12 3,12 0,6" fill="#3bc4cc"/></svg>Coconut Oil Derivatives</li>
    <li><svg viewBox="0 0 13 12"><polygon points="3,0 10,0 13,6 10,12 3,12 0,6" fill="#3bc4cc"/></svg>Lemon Scented</li>
  </ul>
  <p class="company-address">Hartwell Cleaning Supplies 12 Banksia Park Rd.,<br>Northgate 4013. (07) 3900 2750</p>

  <section class="info-column safety-column">
    <p>Wear protective gloves / protective clothing / eye protection / face protection.</p>
    <p><b>IF ON SKIN:</b> Wash with plenty of soap and water.<br><b>IF IN EYES:</b> Rinse cautiously with water for several minutes. Remove contact lenses, if present and easy to do. Continue rinsing.</p>
    <p class="poison-line">Immediately call a POISON CENTRE or doctor / physician.</p>
    <p><span class="rash-title">If skin irritation or rash occurs:</span><br>Get medical advice / attention.</p>
    <p>Take off contaminated clothing and wash before reuse. Dispose of contents / container in accordance with national regulations.</p>
  </section>
  <div class="composition">CONTAINS 10-30%<br>Dodecylbenzenesulponic acid<br>1-10% Sodium Hydroxide</div>

</main>
</body>
</html>
```